Business card for Velvet & Lark weddings and events management company
Velvet & Lark
Business card for Velvet & Lark weddings and events management company - Events
Creative Brief
Modern
Nargiza Huseynova
General Manager
17 Samad Str. AZ 1014, Baku, Azerbaijan
nargiza.huseynova@velvetlark-example.az
www.velvetlark-example.az
In addition to english version, be ready to provide azerbaijani version with little changes in titles as seen below: Name: Nərgizə Hüseynova Title: Müdir Address: Samad küç., 17 AZ1014, Bakı, Azərbaycan Slogan on the back: Sevindirməklə sevinirik! (as seen on azerbaijani version of logo, using only capital letters)
HAPPY TO MAKE YOU HAPPY! SEVİNDİRMƏKLƏ SEVİNİRİK! (on azerbaijani version) for this option, you can provide a different font as well, something maybe handwritten and more friendly. (Original font is Trajan Pro)
tulipwanderer tulipwanderer

```html
<!DOCTYPE html>
<html lang="en">
<head>
<meta charset="utf-8">
<title>Velvet &amp; Lark — Business Card</title>
<link rel="stylesheet" href="https://fonts.googleapis.com/css2?family=Cinzel:wght@400&family=Ubuntu:wght@400;500&display=swap">
<style>
  :root {
    --backdrop: #b9b9b9;
    --card: #ffffff;
    --ink: #111111;
    --muted: #555555;
    --icon: #7a7a7a;
  }
  * { box-sizing: border-box; margin: 0; padding: 0; }
  html, body { width: 1200px; height: 895px; overflow: hidden; }
  body {
    background: var(--backdrop);
    position: relative;
    font-family: "Ubuntu", sans-serif;
    color: var(--ink);
  }
  .card {
    position: absolute;
    width: 540px;
    height: 310px;
    background: var(--card);
    overflow: hidden;
  }
  .card__frame {
    position: absolute;
    inset: 12px;
    border: 2px solid var(--ink);
    pointer-events: none;
  }
  .brand {
    font-family: "Cinzel", serif;
    font-weight: 400;
    color: var(--muted);
    letter-spacing: 1px;
    display: flex;
    align-items: center;
    gap: 10px;
    white-space: nowrap;
  }
  .brand__dot {
    width: 14px; height: 14px;
    border: 2px solid var(--muted);
    border-radius: 50%;
    flex: none;
  }

  /* Logo side */
  .card--logo { left: 600px; top: 110px; }
  .card--logo .lockup {
    position: absolute;
    left: 0; right: 0; top: 72px;
    display: flex;
    flex-direction: column;
    align-items: center;
    gap: 14px;
  }
  .card--logo .brand { font-size: 34px; }
  .slogan {
    font-family: "Cinzel", serif;
    font-size: 13px;
    letter-spacing: 3px;
    color: var(--muted);
    white-space: nowrap;
  }
  .card--logo .band {
    position: absolute;
    left: 0; right: 0; top: 200px;
    height: 54px;
    background: var(--ink);
    display: flex;
    align-items: center;
    justify-content: center;
    padding-left: 60px;
  }
  .card--logo .band__web {
    color: #fff;
    font-size: 19px;
    letter-spacing: 1px;
  }

  /* Info side */
  .card--info { left: 60px; top: 470px; }
  .card--info .band {
    position: absolute;
    left: 0; bottom: 0;
    width: 180px; height: 56px;
    background: var(--ink);
  }
  .card--info .brand {
    position: absolute;
    left: 36px; top: 40px;
    font-size: 26px;
  }
  .contact {
    position: absolute;
    list-style: none;
    font-size: 12.5px;
    color: var(--muted);
  }
  .contact li { display: flex; align-items: center; gap: 10px; height: 26px; white-space: nowrap; }
  .contact svg { width: 16px; height: 16px; flex: none; }
  .contact--left { left: 36px; top: 112px; }
  .contact--right { left: 300px; top: 200px; }
  .person {
    position: absolute;
    left: 300px; top: 128px;
  }
  .person__name { font-size: 15px; font-weight: 500; }
  .person__title { font-size: 12.5px; margin-top: 4px; }
</style>
</head>
<body>

  <section class="card card--logo" aria-label="Business card, logo side">
    <div class="band"><span class="band__web">www.velvetlark-example.az</span></div>
    <div class="card__frame"></div>
    <div class="lockup">
      <div class="brand"><span class="brand__dot"></span>Velvet &amp; Lark</div>
      <p class="slogan">HAPPY TO MAKE YOU HAPPY!</p>
    </div>
  </section>

  <section class="card card--info" aria-label="Business card, contact side">
    <div class="band"></div>
    <div class="card__frame"></div>
    <div class="brand"><span class="brand__dot"></span>Velvet &amp; Lark</div>

    <ul class="contact contact--left">
      <li>
        <svg viewBox="0 0 16 16"><rect width="16" height="16" rx="3" fill="var(--icon)"/><path d="M5 4c1 0 1.5 1.7 1 2.3-.4.4 1.3 2.6 2 2.4.6-.5 2.5 0 2.3 1-.3 1.3-2 1.6-3.8.2C4.7 8.4 3.6 4.2 5 4z" fill="#fff"/></svg>
        010 555 0142
      </li>
      <li>
        <svg viewBox="0 0 16 16"><rect width="16" height="16" rx="3" fill="var(--icon)"/><rect x="3.5" y="5" width="9" height="6.5" fill="none" stroke="#fff" stroke-width="1.2"/><path d="M3.5 5l4.5 3.5L12.5 5" fill="none" stroke="#fff" stroke-width="1.2"/></svg>
        hello@velvetlark-example.az
      </li>
    </ul>

    <div class="person">
      <p class="person__name">Nargiza Huseynova</p>
      <p class="person__title">General Manager</p>
    </div>

    <ul class="contact contact--right">
      <li>
        <svg viewBox="0 0 16 16"><rect width="16" height="16" rx="3" fill="var(--icon)"/><path d="M8 3a3 3 0 0 1 3 3c0 2.2-3 6.5-3 6.5S5 8.2 5 6a3 3 0 0 1 3-3z" fill="#fff"/><circle cx="8" cy="6" r="1.1" fill="var(--icon)"/></svg>
        17 Samad Str. AZ 1014
      </li>
      <li>
        <svg viewBox="0 0 16 16"><rect width="16" height="16" rx="3" fill="var(--icon)"/><circle cx="8" cy="8" r="4.5" fill="none" stroke="#fff" stroke-width="1.1"/><path d="M3.5 8h9M8 3.5c2 2.5 2 6.5 0 9M8 3.5c-2 2.5-2 6.5 0 9" fill="none" stroke="#fff" stroke-width="1"/></svg>
        www.velvetlark-example.az
      </li>
    </ul>
  </section>

</body>
</html>
```